Tovessa Poster

I am looking for a poster to frame for my sister's skin care service business. She treats women of all colors, so i would like a few poster options showing black, white, and latin or asian women.

```html
<!DOCTYPE html>
<html lang="en">
<head>
<meta charset="utf-8">
<title>Tovessa Skin Solutions Poster</title>
<link href="https://fonts.googleapis.com/css2?family=Kaushan+Script&family=Lato:wght@400;700&display=swap" rel="stylesheet">
<style>
  :root {
    --page-bg: #e9e6e2;
    --mint-light: #f1f8ef;
    --mint: #d7ebd3;
    --mint-deep: #bcdcb8;
    --teal: #1fa9a3;
    --teal-dark: #167f7c;
    --leaf-green: #7dbf9c;
    --ink: #141414;
    --photo-grey: #9a9a9a;
  }
  html, body {
    margin: 0;
    padding: 0;
    width: 1200px;
    height: 1200px;
    overflow: hidden;
    background: var(--page-bg);
  }
  .poster {
    position: absolute;
    left: 205px;
    top: 30px;
    width: 790px;
    height: 1140px;
    background: linear-gradient(160deg, var(--mint-light) 0%, var(--mint) 55%, var(--mint-deep) 100%);
    box-shadow: 0 10px 30px rgba(0,0,0,0.18);
    overflow: hidden;
    font-family: 'Lato', sans-serif;
  }
  .corner-foliage {
    position: absolute;
    width: 150px;
    height: 150px;
    background: radial-gradient(circle at center, var(--teal) 0%, var(--teal-dark) 60%, rgba(22,127,124,0) 72%);
  }
  .corner-foliage.top-left { left: -60px; top: 120px; }
  .corner-foliage.top-right { right: -55px; top: -55px; }
  .corner-foliage.bottom-left { left: -55px; bottom: -40px; }
  .corner-foliage.bottom-right { right: -60px; bottom: 200px; }
  .brand {
    position: absolute;
    left: 80px;
    top: 90px;
    display: flex;
    align-items: center;
    gap: 14px;
  }
  .brand-dot {
    width: 22px;
    height: 22px;
    border-radius: 50%;
    background: var(--teal);
  }
  .brand-name {
    font-family: 'Lato', sans-serif;
    font-weight: 400;
    font-size: 30px;
    letter-spacing: 3px;
    color: var(--teal);
    text-transform: uppercase;
  }
  .wreath {
    position: absolute;
    left: 95px;
    top: 190px;
    width: 600px;
    height: 600px;
    border-radius: 50%;
    background: radial-gradient(circle, rgba(125,191,156,0) 62%, rgba(125,191,156,0.75) 70%, rgba(31,169,163,0.45) 80%, rgba(125,191,156,0) 88%);
  }
  .portrait {
    position: absolute;
    left: 165px;
    top: 260px;
    width: 460px;
    height: 460px;
    border-radius: 50%;
    background: radial-gradient(circle at 55% 45%, #f4f4f4 0%, #cfcfcf 45%, var(--photo-grey) 100%);
  }
  .headline {
    position: absolute;
    left: 0;
    right: 0;
    top: 790px;
    text-align: center;
    font-family: 'Kaushan Script', cursive;
    font-size: 72px;
    line-height: 1.05;
    color: var(--ink);
    margin: 0;
  }
  .contact {
    position: absolute;
    left: 0;
    right: 0;
    top: 990px;
    display: flex;
    flex-direction: column;
    align-items: center;
    gap: 14px;
    font-size: 34px;
    color: var(--ink);
  }
  .contact-line {
    display: flex;
    align-items: center;
    gap: 14px;
  }
  .contact-line svg { width: 30px; height: 30px; }
</style>
</head>
<body>
  <main class="poster">
    <div class="corner-foliage top-left" role="img" aria-label="Teal leaf cluster decoration"></div>
    <div class="corner-foliage top-right" role="img" aria-label="Teal leaf cluster decoration"></div>
    <div class="corner-foliage bottom-left" role="img" aria-label="Teal leaf cluster decoration"></div>
    <div class="corner-foliage bottom-right" role="img" aria-label="Teal leaf cluster decoration"></div>

    <div class="brand">
      <span class="brand-dot"></span>
      <span class="brand-name">Tovessa Skin Solutions</span>
    </div>

    <div class="wreath" role="img" aria-label="Watercolour green leaf wreath framing the portrait"></div>
    <div class="portrait" role="img" aria-label="Black and white portrait of a smiling woman touching her cheek"></div>

    <h1 class="headline">Have Your<br>Moment of Tovessa</h1>

    <div class="contact">
      <div class="contact-line">
        <svg viewBox="0 0 24 24" fill="none" stroke="currentColor" stroke-width="1.8">
          <circle cx="12" cy="12" r="10"/>
          <path d="M8.5 7.5c.8-.6 1.6-.4 2 .4l.6 1.3c.3.6.1 1.1-.4 1.5l-.5.4c.5 1.2 1.4 2.1 2.6 2.6l.4-.5c.4-.5.9-.7 1.5-.4l1.3.6c.8.4 1 1.2.4 2-1 1.2-2.6 1.3-4.4.2-1.7-1-3.2-2.5-4.2-4.2-1.1-1.8-1-3.4.2-4.4z"/>
        </svg>
        <span>123 456 7890</span>
      </div>
      <div class="contact-line">
        <svg viewBox="0 0 24 24" fill="none" stroke="currentColor" stroke-width="1.8">
          <circle cx="12" cy="12" r="10"/>
          <ellipse cx="12" cy="12" rx="4.5" ry="10"/>
          <path d="M2 12h20M4 7h16M4 17h16"/>
        </svg>
        <span>www.companyname.com</span>
      </div>
    </div>
  </main>
</body>
</html>
```